Seeking Graphic Designer to Create Catalog for Signage & Branding Company

I am looking to hire a skilled graphic designer to create a professional catalog showcasing the products and services offered by my signage, printing, and branding company. The ideal candidate will review the extensive photo gallery I have provided (link below), select the best high-resolution images, and organize them into thematic sections for our various service offerings.

The specific services we provide include:

- Signage (indoor and outdoor)
- Door signs
- Directory signs and wayfinding
- Digital signage and digital totems
- Printing (banners, flags, posters, catalogs, brochures, stationery)
- Promotional items and branded merchandise
- Exhibitions and displays
- Branding and identity design (logos, brochures, etc.)
- Lightboxes and illuminated displays
- LED lighting for shops and stores
- Exit signs and emergency lighting
- Reflective signs, including custom traffic and road signs

For each service category, the designer should choose 1-3 representative images and craft a concise description highlighting our capabilities. The overall catalog should have a cohesive and visually appealing design theme.

I have provided a link to our photo gallery with hundreds of showcasing past projects and products. Please review this gallery and let me know if you need any additional information or imagery.

As a bonus, the first two designers who submit proposals will receive an additional 10% on the project fee.
https://qv.fz/t-4RkWmaTuZe
https://qv.fz/t-HuzPd2LwoS
https://qv.fz/t-yiTMcbQQLa
https://qv.fz/t-GsraNveoKD
https://qv.fz/t-8BNuFKjwpS
https://qv.fz/t-MVaKpUoW3c
https://qv.fz/t-5GoWLTRBz7
-My instagram may help:
pictoval.com/vantor_kelu
-My facebook may help:
https://www.frendlo.com/vantor.kelu?mibextid=RKPZ7m5

Target Market(s)

Businesses and organizations seeking high-quality signage, printing, and branding services.

Industry/Entity Type

Signage, printing, and branding.

Font styles to use
Sans Serif

Colors
0054AA
0677BA
7BADD7
CADEEF
E8F1F8
FFF300
FFF600
FEFA6F
FFFEC7
FFFEE8
F0912C
F2A743
F7CA91
FBE8D2
FDF5EE
EB3D1F
EC4F4E
F09395
F8D3D4
FCEDEE

Requirements
Must have
• Proficiency in graphic design, attention to detail, and the ability to organize visual content.
Nice to have
• Experience in catalog design, photography skills, and familiarity with the signage, printing, and branding industry.
Should not have
• Lack of responsiveness, inability to work within the specified timeline, or poor communication skills.

```html
<!DOCTYPE html>
<html lang="en">
<head>
<meta charset="utf-8">
<title>Vantor Signs Catalog Cover and Spread</title>
<link rel="stylesheet" href="https://fonts.googleapis.com/css2?family=Arimo:wght@400;700&display=swap">
<style>
  :root {
    --stage: #3b3b3d;
    --yellow: #fcdf22;
    --orange: #f28a30;
    --red: #c9294b;
    --blue: #2f4a8f;
    --navy: #1f3577;
    --white: #ffffff;
    --mist: #e6e7e9;
    --text-orange: #ee7d22;
  }
  * { margin: 0; padding: 0; box-sizing: border-box; }
  html, body { width: 1200px; height: 910px; overflow: hidden; background: var(--stage); font-family: "Arimo", Arial, sans-serif; }
  .canvas { position: relative; width: 1200px; height: 910px; }

  /* outer cover spread */
  .cover-spread { position: absolute; left: 42px; top: 42px; width: 1116px; height: 393px; display: flex; }
  .contact-strip { position: relative; width: 139.5px; height: 393px; color: var(--white); overflow: hidden; }
  .strip-yellow { background: var(--yellow); color: var(--navy); }
  .strip-orange { background: var(--orange); color: var(--navy); }
  .strip-red { background: var(--red); }
  .strip-blue { background: var(--blue); }
  .strip-content {
    position: absolute; left: 50%; top: 50%; width: 393px; height: 139px;
    transform: translate(-50%, -50%) rotate(-90deg);
    display: flex; align-items: center; justify-content: flex-start; gap: 14px; padding-left: 42px;
  }
  .strip-content svg { flex: none; transform: rotate(90deg); }
  .contact-text { font-size: 18px; font-weight: 700; line-height: 1.18; }
  .contact-text.address { font-size: 15.5px; }
  .contact-text.url { font-weight: 400; letter-spacing: 1.5px; font-size: 17px; }

  .front-cover { position: relative; width: 558px; height: 393px; background: linear-gradient(90deg, #ffffff 0%, #ececee 100%); overflow: hidden; }
  .brand-lockup { position: absolute; left: 150px; top: 72px; display: flex; align-items: center; gap: 14px; }
  .brand-dot { width: 58px; height: 58px; border-radius: 50%; background: var(--orange); }
  .brand-name { font-size: 44px; font-weight: 700; color: var(--blue); line-height: 1; }
  .service-band { position: absolute; left: 0; top: 198px; width: 558px; height: 195px; background: var(--blue); }
  .service-pills { position: absolute; left: 0; top: 198px; }
  .pill-label { font-family: "Arimo", Arial, sans-serif; font-weight: 700; font-size: 17px; }
  .cover-url { position: absolute; left: 0; right: 0; top: 356px; text-align: center; color: var(--white); font-size: 17px; letter-spacing: 2px; }

  /* inner spread */
  .inner-spread { position: absolute; left: 42px; top: 474px; width: 1116px; height: 394px; background: linear-gradient(90deg, #ffffff 0%, #ffffff 52%, #ececee 54%, #ffffff 100%); overflow: hidden; }
  .side-band { position: absolute; top: 0; width: 64px; height: 394px; background: var(--blue); color: var(--white); }
  .side-band.left { left: 0; }
  .side-band.right { right: 0; }
  .side-stripe { position: absolute; top: 0; width: 6px; height: 394px; background: linear-gradient(180deg, var(--yellow) 0 33%, var(--orange) 33% 66%, var(--red) 66% 100%); }
  .side-stripe.left { left: 64px; }
  .side-stripe.right { right: 65px; }
  .side-url { position: absolute; left: 50%; font-size: 12px; letter-spacing: 1px; white-space: nowrap; }
  .side-band.left .side-url { top: 30px; transform: translateX(-50%) rotate(-90deg) translateX(-50%); transform-origin: center; top: 100px; }
  .side-band.right .side-url { top: 300px; transform: translateX(-50%) rotate(90deg); }
  .side-brand { position: absolute; left: 50%; display: flex; align-items: center; gap: 5px; white-space: nowrap; font-size: 12px; font-weight: 700; }
  .side-brand span.dot { width: 10px; height: 10px; border-radius: 50%; background: var(--white); }
  .side-band.left .side-brand { top: 330px; transform: translateX(-50%) rotate(-90deg); }
  .side-band.right .side-brand { top: 50px; transform: translateX(-50%) rotate(90deg); }

  .section-kicker { position: absolute; font-size: 15px; font-weight: 700; color: var(--text-orange); }
  .section-title { position: absolute; font-size: 29px; font-weight: 700; color: var(--navy); }
  .kicker-left { left: 90px; top: 28px; }
  .title-left { left: 90px; top: 50px; }
  .kicker-right { right: 90px; top: 28px; }
  .title-right { right: 90px; top: 50px; }
  .gallery { position: absolute; left: 86px; top: 86px; }
</style>
</head>
<body>
<div class="canvas">

  <section class="cover-spread">
    <div class="contact-strip strip-yellow">
      <div class="strip-content">
        <svg width="22" height="20" viewBox="0 0 22 20" aria-hidden="true"><rect x="1" y="2" width="20" height="16" fill="none" stroke="#1f3577" stroke-width="2.2"/><path d="M1 2 L11 11 L21 2 M1 18 L8 10 M21 18 L14 10" fill="none" stroke="#1f3577" stroke-width="2"/></svg>
        <span class="contact-text">hello@vantorsigns.com</span>
      </div>
    </div>
    <div class="contact-strip strip-orange">
      <div class="strip-content">
        <svg width="24" height="24" viewBox="0 0 24 24" aria-hidden="true"><path d="M6 3 L10 7 L8 10 C9 13 11 15 14 16 L17 14 L21 18 L18 21 C10 20 4 14 3 6 Z" fill="#1f3577"/></svg>
        <span class="contact-text">+234800 555 0147</span>
      </div>
    </div>
    <div class="contact-strip strip-red">
      <div class="strip-content">
        <svg width="22" height="28" viewBox="0 0 22 28" aria-hidden="true"><path d="M11 1 C5 1 1 5 1 11 C1 18 11 27 11 27 C11 27 21 18 21 11 C21 5 17 1 11 1 Z" fill="#fff"/><circle cx="11" cy="11" r="4" fill="#c9294b"/></svg>
        <span class="contact-text address">Vantor Signs (Nig) LTD No.4,<br>Kelu Plaza Plot 2210,<br>Orchid Lane Maitama,<br>Abuja, Nigeria</span>
      </div>
    </div>
    <div class="contact-strip strip-blue">
      <div class="strip-content">
        <svg width="26" height="26" viewBox="0 0 26 26" aria-hidden="true"><circle cx="13" cy="13" r="11.5" fill="none" stroke="#fff" stroke-width="2"/><ellipse cx="13" cy="13" rx="5" ry="11.5" fill="none" stroke="#fff" stroke-width="2"/><path d="M1.5 13 H24.5 M3.5 7 H22.5 M3.5 19 H22.5" stroke="#fff" stroke-width="2"/></svg>
        <span class="contact-text url">www.vantorsigns.com</span>
      </div>
    </div>

    <div class="front-cover">
      <div class="brand-lockup">
        <span class="brand-dot"></span>
        <span class="brand-name">Vantor Signs</span>
      </div>
      <div class="service-band"></div>
      <svg class="service-pills" width="558" height="140" viewBox="0 0 558 140">
        <path d="M0 0 H468 A70 70 0 0 1 468 140 H0 Z" fill="#e9cc2c" stroke="#fff" stroke-width="3" role="img" aria-label="Photo of branded building wall"/>
        <path d="M0 0 H310 A70 70 0 0 1 310 140 H0 Z" fill="#f0913a" stroke="#fff" stroke-width="3" role="img" aria-label="Photo of print workshop"/>
        <path d="M0 0 H134 A70 70 0 0 1 134 140 H0 Z" fill="#d0435c" stroke="#fff" stroke-width="3" role="img" aria-label="Photo of sign fabrication"/>
        <text class="pill-label" x="56" y="76" fill="#fff">SIGNAGE</text>
        <text class="pill-label" x="246" y="76" fill="#1a1a1a">PRINTING</text>
        <text class="pill-label" x="424" y="76" fill="#1a1a1a">Branding</text>
      </svg>
      <div class="cover-url">www.vantorsigns.com</div>
    </div>
  </section>

  <section class="inner-spread">
    <div class="side-band left">
      <span class="side-url">www.vantorsigns.com</span>
      <span class="side-brand"><span class="dot"></span>Vantor Signs</span>
    </div>
    <div class="side-stripe left"></div>
    <div class="side-stripe right"></div>
    <div class="side-band right">
      <span class="side-brand"><span class="dot"></span>Vantor Signs</span>
      <span class="side-url">www.vantorsigns.com</span>
    </div>

    <p class="section-kicker kicker-left">DIGITAL SIGNAGE AND</p>
    <h2 class="section-title title-left">DIGITAL TOTEMS</h2>
    <p class="section-kicker kicker-right">(Banners, Flags, Posters, Catalogs, Brochures, Stationery)</p>
    <h2 class="section-title title-right">PRINTING</h2>

    <svg class="gallery" width="944" height="264" viewBox="0 0 944 264">
      <defs>
        <clipPath id="capsule"><rect x="0" y="0" width="944" height="264" rx="132" ry="132"/></clipPath>
      </defs>
      <g clip-path="url(#capsule)">
        <rect x="0" y="0" width="234" height="130" fill="#c9d3e0" role="img" aria-label="Photo of printed backdrop wall"/>
        <rect x="238" y="0" width="232" height="130" fill="#5a5e66" role="img" aria-label="Photo of illuminated letter samples"/>
        <rect x="472" y="0" width="258" height="130" fill="#b9bec4" role="img" aria-label="Photo of printed site hoarding"/>
        <rect x="734" y="0" width="210" height="130" fill="#8a8f96" role="img" aria-label="Photo of directory sign board"/>
        <rect x="0" y="135" width="190" height="129" fill="#9aa6b0" role="img" aria-label="Photo of digital totem display"/>
        <rect x="196" y="135" width="226" height="129" fill="#55595f" role="img" aria-label="Photo of lightbox sign"/>
        <rect x="424" y="135" width="226" height="129" fill="#6c6f75" role="img" aria-label="Photo of roadside welcome banner"/>
        <rect x="654" y="135" width="290" height="129" fill="#b8a690" role="img" aria-label="Photo of festive printed banner"/>
      </g>
    </svg>
  </section>

</div>
</body>
</html>
```